Tallgrove Vale Management

I need a professional website. My current website is tallgrovevalemanagement.com and I hate it. It was created with some AI tool very quickly because I needed a site up and running with no advanced notice. I’m open to all designs .. I trust you, the professionals will deliver the results I’m anxiously awaiting! :)

```html
<!DOCTYPE html>
<html lang="en">
<head>
<meta charset="utf-8">
<title>Tallgrove Vale Management</title>
<link rel="stylesheet" href="https://fonts.googleapis.com/css2?family=Roboto:wght@400;500;700;900&family=Poppins:ital,wght@0,400;0,500;0,600;0,700;1,400&display=swap">
<style>
:root{
  --red:#d1272f;
  --navy:#1f3361;
  --navy-soft:#33476f;
  --ink:#1d1d1f;
  --muted:#444;
  --line:#e3e3e3;
  --white:#fff;
  --gold:#f2b01e;
}
*{margin:0;padding:0;box-sizing:border-box}
html,body{width:1200px;height:4967px;overflow:hidden;background:var(--white)}
body{position:relative;font-family:"Poppins",sans-serif;color:var(--ink)}
.abs{position:absolute}
.heading{font-family:"Roboto",sans-serif;font-weight:700;color:var(--navy);line-height:1.15}
.eyebrow{font-family:"Poppins",sans-serif;font-size:21px;color:var(--red);letter-spacing:.5px;display:flex;align-items:center;gap:8px;text-transform:uppercase}
.eyebrow::before{content:"";width:58px;height:2px;background:var(--red)}
.eyebrow.centered::after{content:"";width:58px;height:2px;background:var(--red)}
.btn{position:absolute;display:flex;align-items:center;justify-content:center;background:var(--red);color:var(--white);font-family:"Poppins",sans-serif;font-weight:600;font-size:19px;border-radius:0 14px 0 14px;text-transform:uppercase}
.photo{position:absolute}

/* header */
.brand-badge{left:73px;top:0;width:177px;height:193px;background:var(--white);border-radius:0 0 40px 40px;box-shadow:0 6px 18px rgba(0,0,0,.15);display:flex;flex-direction:column;align-items:center;justify-content:center;gap:10px;z-index:3}
.brand-mark{width:26px;height:26px;background:var(--navy)}
.brand-name{font-family:"Roboto",sans-serif;font-weight:900;color:var(--navy);font-size:21px;line-height:1.1;text-align:center}
.main-nav{left:544px;top:33px;width:591px;height:46px;border:2px solid var(--navy);border-radius:23px;display:flex;align-items:center;justify-content:space-around;padding:0 12px;font-size:13px;font-weight:500;color:var(--ink)}
.main-nav .active{background:var(--red);color:var(--white);padding:7px 14px;border-radius:16px;font-weight:600}

/* hero */
.hero{left:0;top:106px;width:1200px;height:801px}
.hero-title{left:665px;top:250px;font-family:"Roboto",sans-serif;font-weight:700;font-size:74px;line-height:87px;color:var(--white)}
.hero-btn{left:665px;top:604px;width:242px;height:76px;background:var(--navy);font-size:22px}

/* about */
.about-copy{left:68px;top:1022px;width:528px}
.about-copy h2{font-size:49px;margin-top:14px}
.about-lead{font-size:14.5px;font-weight:600;line-height:26px;margin-top:20px;text-align:justify}
.about-copy p.body{font-size:13.3px;line-height:26px;color:var(--muted);margin-top:12px;text-align:justify}
.oval{border-radius:999px;overflow:hidden}

/* services */
.services-head{left:0;top:1690px;width:1200px;text-align:center}
.services-head .eyebrow{justify-content:center}
.services-head h2{font-size:59px;margin-top:4px}
.services-head p{font-size:14.5px;line-height:27px;color:var(--muted);width:1000px;margin:22px auto 0}
.card{position:absolute;top:1916px;width:341px;height:352px;border-radius:16px;background:var(--white);box-shadow:0 4px 14px rgba(0,0,0,.16);overflow:hidden}
.card .photo{left:0;top:0;width:100%;height:280px}
.card h3{position:absolute;left:0;right:0;top:292px;text-align:center;font-family:"Roboto",sans-serif;font-weight:500;font-size:29px;color:var(--ink)}
.card.featured{background:linear-gradient(180deg,#33476f,#2d406a 60%,#3a4d74);color:var(--white);text-align:center;padding:64px 34px 0}
.card.featured h3{position:static;color:var(--white);font-size:29px;line-height:1.1}
.card.featured p{font-size:14px;line-height:27px;margin-top:18px}
.card.featured .link{display:inline-block;margin-top:14px;font-size:14px;font-weight:500;border-bottom:1px solid var(--white)}
.arrow-btn{position:absolute;width:58px;height:58px;border-radius:50%;border:2px solid var(--red);display:flex;align-items:center;justify-content:center}
.arrow-btn.filled{background:var(--red)}

/* testimonials */
.testi-head{left:89px;top:2548px}
.testi-head h2{font-size:51px;margin-top:4px}
.review{position:absolute;top:2532px;width:323px;height:253px;background:var(--white);box-shadow:0 3px 12px rgba(0,0,0,.14);padding:34px 26px}
.review p{font-style:italic;font-size:14px;line-height:24px;color:#333;text-align:justify}
.reviewer{position:absolute;left:26px;top:178px;display:flex;align-items:center;gap:12px}
.avatar{width:64px;height:64px;border-radius:50%}
.reviewer strong{display:block;color:var(--red);font-weight:600;font-size:17px}
.stars{color:var(--gold);font-size:13px;letter-spacing:1px}
.quote{position:absolute;right:26px;top:196px}

/* cta */
.cta{left:68px;top:2962px;width:1067px;height:685px;border-radius:60px;overflow:hidden}
.cta h2{position:absolute;left:0;right:0;top:330px;text-align:center;font-size:82px;line-height:1.1}
.cta-btn{left:412px;top:535px;width:240px;height:73px;font-size:22px}

/* contact */
.contact-head{left:652px;top:3815px}
.contact-head h2{font-size:59px;margin-top:2px}
.field{position:absolute;background:var(--white);border:1px solid var(--line);box-shadow:0 2px 6px rgba(0,0,0,.08);font-size:13px;color:#777;padding:14px 20px}

/* footer */
.footer-title{font-family:"Roboto",sans-serif;font-weight:500;font-size:22px;color:var(--white);position:absolute}
.footer-title::after{content:"";display:block;width:30px;height:2px;background:var(--white);margin-top:8px}
.foot-links{list-style:none;color:var(--white);font-size:14px}
.foot-links li{height:26px;display:flex;align-items:center;gap:12px}
.foot-links li::before{content:"";width:8px;height:8px;border-radius:50%;border:2px solid var(--white)}
.contact-item{position:absolute;left:554px;display:flex;gap:18px;color:var(--white);font-size:14px;line-height:17px}
.ci-icon{width:28px;height:28px;border:2px solid var(--white);background:var(--navy);display:flex;align-items:center;justify-content:center;border-radius:4px}
.social{position:absolute;top:4922px;width:28px;height:28px;border-radius:50%;background:var(--red);border:2px solid var(--white)}

/* photo fills */
.fill-bath{background:
  radial-gradient(ellipse 40% 22% at 30% 22%,rgba(240,228,205,.9),transparent 70%),
  radial-gradient(ellipse 70% 30% at 55% 62%,rgba(214,196,170,.95),transparent 75%),
  linear-gradient(90deg,#5e554c 0%,#b9ada0 18%,#d6ccc0 45%,#c2b6a8 75%,#8f8377 100%)}
.fill-tap{background:
  radial-gradient(ellipse 60% 25% at 40% 18%,rgba(70,60,52,.85),transparent 75%),
  radial-gradient(ellipse 70% 35% at 50% 75%,rgba(230,218,200,.9),transparent 75%),
  linear-gradient(180deg,#6e655c 0%,#b8ab9b 40%,#d8cdbd 70%,#c7baa8 100%)}
.fill-samples{background:
  radial-gradient(ellipse 35% 30% at 30% 35%,rgba(230,220,205,.85),transparent 70%),
  radial-gradient(ellipse 22% 15% at 68% 22%,rgba(196,110,70,.7),transparent 70%),
  radial-gradient(ellipse 30% 30% at 12% 70%,rgba(150,100,70,.8),transparent 75%),
  linear-gradient(150deg,#2f241c 0%,#6b5240 25%,#b99574 55%,#dcc3a3 100%)}
.fill-desk{background:
  radial-gradient(ellipse 18% 30% at 75% 30%,rgba(246,242,232,.95),transparent 70%),
  radial-gradient(ellipse 15% 10% at 42% 62%,rgba(200,120,80,.7),transparent 70%),
  linear-gradient(90deg,#9d7b5c 0%,#bba58f 18%,#d9d3cc 40%,#cfc8c0 75%,#6e6259 100%)}
.fill-house{background:
  radial-gradient(ellipse 26% 24% at 50% 30%,rgba(160,110,70,.65),transparent 70%),
  radial-gradient(ellipse 45% 12% at 48% 43%,rgba(230,222,210,.9),transparent 75%),
  linear-gradient(180deg,#8b7f73 0%,#b9a896 25%,#e2d3c1 55%,#f1e6d8 100%)}
.fill-blocks-a{background:
  radial-gradient(ellipse 40% 28% at 55% 55%,rgba(208,170,125,.9),transparent 72%),
  linear-gradient(160deg,#9e958c,#cdc5bb 60%,#b2a796)}
.fill-blocks-b{background:
  radial-gradient(ellipse 45% 14% at 45% 32%,rgba(215,212,205,.95),transparent 72%),
  radial-gradient(ellipse 40% 26% at 42% 55%,rgba(212,172,125,.95),transparent 72%),
  linear-gradient(170deg,#7d756d,#c3b8a9 55%,#ddd3c5)}
</style>
</head>
<body>

<!-- hero -->
<svg class="hero abs" viewBox="0 0 1200 801" width="1200" height="801">
  <defs>
    <linearGradient id="heroWall" x1="0" y1="0" x2="1" y2="0">
      <stop offset="0" stop-color="#a9a299"/>
      <stop offset=".5" stop-color="#8a847c"/>
      <stop offset="1" stop-color="#4f4b46"/>
    </linearGradient>
    <linearGradient id="heroFloor" x1="0" y1="0" x2="0" y2="1">
      <stop offset="0" stop-color="#b5aea5" stop-opacity="0"/>
      <stop offset=".15" stop-color="#c7c0b6"/>
      <stop offset="1" stop-color="#a49c92"/>
    </linearGradient>
    <radialGradient id="heroGlow" cx="300" cy="330" r="240" gradientUnits="userSpaceOnUse">
      <stop offset="0" stop-color="#f1ede7"/>
      <stop offset=".55" stop-color="#d8d2ca" stop-opacity=".85"/>
      <stop offset="1" stop-color="#d8d2ca" stop-opacity="0"/>
    </radialGradient>
  </defs>
  <g role="img" aria-label="Sculpted white sphere resting on a grey surface">
    <polygon points="0,0 1200,0 1200,652 600,772 0,652" fill="url(#heroWall)"/>
    <polygon points="0,440 1200,440 1200,652 600,772 0,652" fill="url(#heroFloor)"/>
    <polygon points="0,0 1200,0 1200,652 600,772 0,652" fill="url(#heroGlow)"/>
  </g>
  <polygon points="0,652 600,772 1200,652 1200,685 600,801 0,685" fill="#1f3361"/>
  <polygon points="605,58 1200,128 1200,570 605,679" fill="#d1272f"/>
</svg>

<header>
  <div class="brand-badge abs">
    <span class="brand-mark"></span>
    <span class="brand-name">TALLGROVE VALE<br>MANAGEMENT</span>
  </div>
  <nav class="main-nav abs">
    <span class="active">HOME</span><span>ABOUT US</span><span>SERVICES</span><span>TESTIMONIALS</span><span>CONTACT US</span>
  </nav>
</header>

<h1 class="hero-title abs">A TRUE<br>TALLGROVE<br>NOT JUST<br>A VENDOR.</h1>
<a class="btn hero-btn">Learn More</a>

<!-- about -->
<section class="about-copy abs">
  <div class="eyebrow">Who We Are</div>
  <h2 class="heading">About Our Property Management Solutions</h2>
  <p class="about-lead">Our organization delivers comprehensive property management solutions that optimize asset performance and tenant satisfaction.</p>
  <p class="body">By integrating advanced analytics with proven operational frameworks, our specialists ensure each property achieves sustained value appreciation.</p>
  <p class="body" style="margin-top:20px">Drawing on decades of collective expertise, the team facilitates regulatory compliance, cost efficiency, and proactive maintenance. This disciplined approach enables owners to preserve capital, enhance occupancy rates, and demonstrate long-term resilience across diverse market conditions.</p>
</section>
<a class="btn" style="left:68px;top:1474px;width:177px;height:54px;font-size:17px">Read More</a>
<div class="photo oval fill-bath" role="img" aria-label="Modern bathroom sink with brass faucet" style="left:627px;top:1032px;width:276px;height:488px"></div>
<div class="photo oval fill-tap" role="img" aria-label="Close-up of a tall faucet against a warm wall" style="left:920px;top:1113px;width:215px;height:373px"></div>

<!-- services -->
<section class="services-head abs">
  <div class="eyebrow centered">What We Do</div>
  <h2 class="heading">Our Services</h2>
  <p>Our analysis demonstrates that effective property oversight originates from meticulous operational planning, transparent communication channels, and data-driven performance metrics across every asset class.</p>
</section>
<article class="card" style="left:68px">
  <div class="photo fill-samples" role="img" aria-label="Hands arranging material samples on a wooden table"></div>
  <h3>Basic Service</h3>
</article>
<article class="card featured" style="left:432px">
  <h3>Intermediate<br>Service</h3>
  <p>Describe important details like price, value, length of service, and why it's unique.</p>
  <span class="link">VIEW DETAILS</span>
</article>
<article class="card" style="left:793px">
  <div class="photo fill-desk" role="img" aria-label="Bright desk with lamp, laptop and flowers"></div>
  <h3>Advanced Service</h3>
</article>
<div class="arrow-btn" style="left:536px;top:2330px"><svg width="16" height="16" viewBox="0 0 16 16"><path d="M10 3 5 8l5 5" fill="none" stroke="#d1272f" stroke-width="2.5"/></svg></div>
<div class="arrow-btn filled" style="left:606px;top:2330px"><svg width="16" height="16" viewBox="0 0 16 16"><path d="M6 3l5 5-5 5" fill="none" stroke="#fff" stroke-width="2.5"/></svg></div>

<!-- testimonials -->
<section class="testi-head abs">
  <div class="eyebrow">Client Reviews</div>
  <h2 class="heading">Testimonials</h2>
</section>
<div class="arrow-btn" style="left:88px;top:2730px;width:52px;height:52px"><svg width="14" height="14" viewBox="0 0 16 16"><path d="M10 3 5 8l5 5" fill="none" stroke="#d1272f" stroke-width="2.5"/></svg></div>
<div class="arrow-btn filled" style="left:150px;top:2730px;width:52px;height:52px"><svg width="14" height="14" viewBox="0 0 16 16"><path d="M6 3l5 5-5 5" fill="none" stroke="#fff" stroke-width="2.5"/></svg></div>

<article class="review" style="left:457px">
  <p>Lorem ipsum dolor sit amet, consecte tur adipiscing elit. Pellentesque aliquet eros vitae placerat hendrerit. Maece nas maximus commodo sapien, vitae lobortis ligula</p>
  <div class="reviewer"><span class="avatar" role="img" aria-label="Client portrait" style="background:radial-gradient(circle at 50% 40%,#8a6448,#4a3226 75%)"></span><div><strong>Marcus Hale</strong><span class="stars">★★★★★</span></div></div>
  <svg class="quote" width="44" height="34" viewBox="0 0 44 34"><path d="M0 0h18v18l-8 16H2l6-16H0zM24 0h18v18l-8 16h-8l6-16h-8z" fill="#d1272f"/></svg>
</article>
<article class="review" style="left:812px">
  <p>Lorem ipsum dolor sit amet, consecte tur adipiscing elit. Pellentesque aliquet eros vitae placerat hendrerit. Maece nas maximus commodo sapien, vitae lobortis ligula</p>
  <div class="reviewer"><span class="avatar" role="img" aria-label="Client portrait" style="background:radial-gradient(circle at 50% 40%,#e2c8ac,#b08a66 75%)"></span><div><strong>Dana Orwell</strong><span class="stars">★★★★★</span></div></div>
  <svg class="quote" width="44" height="34" viewBox="0 0 44 34"><path d="M0 0h18v18l-8 16H2l6-16H0zM24 0h18v18l-8 16h-8l6-16h-8z" fill="#d1272f"/></svg>
</article>

<!-- call to action -->
<section class="cta abs fill-house" role="img" aria-label="Architectural model of a modern house on a soft beige backdrop">
  <h2 class="heading">Submit Your Property<br>Management Inquiry</h2>
  <a class="btn cta-btn">Contact Us</a>
</section>

<!-- contact -->
<div class="photo oval fill-blocks-a" role="img" aria-label="Stacked timber blocks under a concrete slab" style="left:79px;top:3908px;width:218px;height:376px"></div>
<div class="photo oval fill-blocks-b" role="img" aria-label="Stacked timber blocks under a concrete slab, close view" style="left:311px;top:3831px;width:278px;height:486px"></div>
<section class="contact-head abs">
  <div class="eyebrow">Get In Touch</div>
  <h2 class="heading">Contact Us</h2>
</section>
<div class="field" style="left:652px;top:3952px;width:220px;height:43px;padding-top:12px">First Name:</div>
<div class="field" style="left:892px;top:3952px;width:223px;height:43px;padding-top:12px">Last Name:</div>
<div class="field" style="left:652px;top:4014px;width:220px;height:46px;padding-top:13px">Phone:</div>
<div class="field" style="left:892px;top:4014px;width:223px;height:46px;padding-top:13px">Email:</div>
<div class="field" style="left:652px;top:4080px;width:463px;height:142px;padding-top:22px">Mesage:</div>
<a class="btn" style="left:652px;top:4253px;width:178px;height:51px;font-size:17px">Submit Now</a>

<!-- footer -->
<svg class="abs" style="left:0;top:4420px" width="1200" height="547" viewBox="0 0 1200 547">
  <polygon points="0,125 600,9 1200,125 1200,163 600,47 0,163" fill="#1f3361"/>
  <polygon points="0,172 600,56 1200,172 1200,482 0,482" fill="#d1272f"/>
  <rect x="0" y="482" width="1200" height="65" fill="#1f3361"/>
</svg>

<div class="brand-badge abs" style="left:77px;top:4642px;width:193px;height:203px;border-radius:0 0 40px 40px">
  <span class="brand-mark"></span>
  <span class="brand-name">TALLGROVE VALE<br>MANAGEMENT</span>
</div>

<div class="footer-title" style="left:344px;top:4648px">Quick Links</div>
<ul class="foot-links abs" style="left:344px;top:4713px">
  <li>About Us</li><li>Services</li><li>Testimonials</li><li>Contact Us</li>
</ul>

<div class="footer-title" style="left:554px;top:4648px">Contact Us</div>
<div class="contact-item" style="top:4722px">
  <span class="ci-icon"><svg width="14" height="14" viewBox="0 0 16 16"><path d="M4 1 6.5 4 5 6c1 2 3 4 5 5l2-1.5 3 2.5-2 3C7 15 1 9 1 3z" fill="#fff"/></svg></span>
  <span>CALL US<br>012 345 6789</span>
</div>
<div class="contact-item" style="top:4774px">
  <span class="ci-icon"><svg width="14" height="12" viewBox="0 0 16 12"><rect x="0.5" y="0.5" width="15" height="11" fill="none" stroke="#fff"/><path d="M1 1l7 6 7-6" fill="none" stroke="#fff"/></svg></span>
  <span>EMAIL US<br>info@tallgrovevalemanagement.com</span>
</div>
<div class="contact-item" style="top:4822px">
  <span class="ci-icon"><svg width="12" height="15" viewBox="0 0 12 16"><path d="M6 0a6 6 0 0 0-6 6c0 4 6 10 6 10s6-6 6-10a6 6 0 0 0-6-6zm0 8.5a2.5 2.5 0 1 1 0-5 2.5 2.5 0 0 1 0 5z" fill="#fff"/></svg></span>
  <span>Address line Dummy here<br>Address line dummy</span>
</div>

<div class="footer-title" style="left:925px;top:4648px">Our Newsletter</div>
<p class="abs" style="left:925px;top:4718px;width:200px;color:#fff;font-size:13px;line-height:17px">Subscribe our newsletter to get the latest news.</p>
<div class="abs" style="left:926px;top:4773px;width:193px;height:29px;background:#fff"></div>
<div class="abs" style="left:924px;top:4823px;width:99px;height:27px;background:var(--navy);border:1px solid #fff;color:#fff;font-size:10px;display:flex;align-items:center;justify-content:center;font-weight:500">SUBSCRIBE</div>

<p class="abs" style="left:68px;top:4928px;color:#fff;font-size:12px">Copyright © 2026 All Rights Reserved By Company name</p>
<span class="social" style="left:1011px"></span>
<span class="social" style="left:1042px"></span>
<span class="social" style="left:1074px"></span>
<span class="social" style="left:1105px"></span>

</body>
</html>
```